Cool blackchain based app company needs a website :)

pillcheckhub.net

Kinda says it all!! This is an app which sits on your smartfone / tablet. You scan a QR code from a medicinal product and our app will verify if the product you have is genuine. It's simple, It's free.

The design could be very modern and simple. It should show in graphical form how the app works and have FAQ's etc.

pillcheckhub.net is designed specifically to allow consumers verify that the medical products which they have purchased are genuine.

Detailed brief with content attached. Logo in high res and QR code attached.

Full website required.
Updates

Target Market(s)

Pharmaceutical

Industry/Entity Type

Pharmaceutical

Coding

Coded - Design and coding required

Number of Pages Required

3 page

Colors

Designer to choose colors to be used in the design.

Requirements
Must have
• Strong visuals - very simple navigation - 3 pages
Nice to have
• Animation of the process
Should not have
• Jargon!

```html
<!DOCTYPE html>
<html lang="en">
<head>
<meta charset="utf-8">
<title>pillcheckhub.net</title>
<link href="https://fonts.googleapis.com/css2?family=Roboto:wght@400;500&family=Roboto+Condensed:wght@400;500&family=Kalam:wght@300&display=swap" rel="stylesheet">
<style>
  :root {
    --white: #ffffff;
    --ink: #2b2b2b;
    --muted: #6b6b6b;
    --brand-green: #2f7d3a;
    --brand-blue: #1f5d99;
    --button-blue: #1f5aa6;
    --bubble-blue: #5db8ee;
    --bar-grey: #f1f1f1;
    --rule: #dcdcdc;
    --social-a: #3b5998;
    --social-b: #2fa9e0;
    --social-c: #dd4b39;
  }
  * { box-sizing: border-box; margin: 0; padding: 0; }
  html, body { width: 1200px; height: 676px; overflow: hidden; background: var(--white); }
  body { font-family: "Roboto", Arial, sans-serif; color: var(--ink); }

  .site { position: relative; width: 1200px; height: 676px; }

  .site-header {
    height: 70px; display: flex; align-items: center;
    padding: 0 60px 0 40px; background: var(--white);
  }
  .brand { display: flex; align-items: center; gap: 10px; width: 360px; }
  .brand-dot { width: 40px; height: 40px; border-radius: 50%; background: var(--brand-green); }
  .brand-name { font-size: 21px; font-weight: 500; color: var(--brand-blue); }
  .main-nav { display: flex; gap: 36px; font-size: 13px; color: var(--ink); flex: 1; padding-left: 40px; }
  .header-actions { display: flex; align-items: center; gap: 14px; font-size: 13px; }
  .chat-link { display: flex; align-items: center; gap: 5px; }
  .btn-primary {
    background: var(--button-blue); color: var(--white); font-family: "Roboto Condensed", sans-serif;
    font-size: 14px; padding: 8px 12px; border-radius: 3px;
  }

  .hero { position: relative; height: 450px; overflow: hidden; }
  .hero-photo {
    position: absolute; inset: 0;
    background: linear-gradient(100deg, #3a2a22 0%, #6c7f95 30%, #8ea4bb 55%, #3f3a38 80%, #2a2624 100%);
  }
  .hero-shade { position: absolute; inset: 0; background: rgba(0,0,0,0.22); }
  .scan-bubble {
    position: absolute; left: 278px; top: 36px;
    background: var(--bubble-blue); color: var(--white);
    font-family: "Roboto Condensed", sans-serif; font-size: 20px;
    padding: 12px 14px;
  }
  .scan-bubble::after {
    content: ""; position: absolute; left: 80px; bottom: -9px;
    border-left: 8px solid transparent; border-right: 8px solid transparent;
    border-top: 9px solid var(--bubble-blue);
  }
  .hero-copy { position: absolute; left: 0; right: 0; top: 160px; text-align: center; color: var(--white); }
  .hero-tagline { font-family: "Kalam", cursive; font-weight: 300; font-size: 30px; margin-bottom: 18px; }
  .hero-lead { font-family: "Roboto Condensed", sans-serif; font-size: 13px; line-height: 21px; }
  .btn-outline {
    display: inline-block; margin-top: 22px; border: 2px solid var(--white); border-radius: 3px;
    font-family: "Roboto Condensed", sans-serif; font-size: 14px; padding: 8px 12px;
  }

  .info-bar {
    height: 34px; background: var(--bar-grey); border-bottom: 1px solid var(--rule);
    display: flex; align-items: center; padding: 0 36px 0 90px; font-size: 12px; color: var(--muted);
  }
  .info-links { display: flex; gap: 24px; flex: 1; }
  .info-label { margin-right: -14px; color: #555; }
  .social { display: flex; gap: 22px; align-items: center; }
  .social-square { width: 14px; height: 14px; border-radius: 2px; }
  .sq-a { background: var(--social-a); } .sq-b { background: var(--social-b); } .sq-c { background: var(--social-c); }

  .intro { text-align: center; padding-top: 12px; }
  .intro-title { font-size: 20px; font-weight: 400; line-height: 28px; }
  .intro-text { font-size: 11.5px; line-height: 17px; margin-top: 8px; color: var(--ink); }
</style>
</head>
<body>
<div class="site">
  <header class="site-header">
    <div class="brand"><span class="brand-dot"></span><span class="brand-name">pillcheckhub.net</span></div>
    <nav class="main-nav"><span>How it Works</span><span>FAQ's</span><span>Our Team</span></nav>
    <div class="header-actions">
      <span class="chat-link">Chat
        <svg width="12" height="10" viewBox="0 0 12 10"><path d="M1 1h10v6H5l-3 2V7H1z" fill="none" stroke="#2b2b2b" stroke-width="1.2"/></svg>
      </span>
      <span class="btn-primary">Scan a QR Code</span>
    </div>
  </header>

  <section class="hero">
    <div class="hero-photo" role="img" aria-label="Photo of two young people in a café checking their smartphones"></div>
    <div class="hero-shade"></div>
    <div class="scan-bubble">pillcheckhub.net/scan_QR</div>
    <div class="hero-copy">
      <p class="hero-tagline">Its Quick, Its Secure, Its Free</p>
      <p class="hero-lead">30% of all medicine bought online is counterfeit<br>Are you sure that the medication you take is genuine?</p>
      <span class="btn-outline">Scan a QR Code</span>
    </div>
  </section>

  <div class="info-bar">
    <div class="info-links"><span class="info-label">Learn More:</span><span>Our Company</span><span>Blog</span><span>Careers</span><span>Help &amp; Contact</span></div>
    <div class="social">
      <span class="social-square sq-a"></span><span class="social-square sq-b"></span><span class="social-square sq-c"></span>
      <svg width="12" height="12" viewBox="0 0 12 12"><circle cx="5" cy="5" r="3.6" fill="none" stroke="#777" stroke-width="1.5"/><path d="M7.6 7.6L11 11" stroke="#777" stroke-width="1.6"/></svg>
    </div>
  </div>

  <section class="intro">
    <h2 class="intro-title">Be Safe, Authenticate<br>Protect your health with pillcheckhub</h2>
    <p class="intro-text">Scan the pillcheckhub QR code which is printed on your medication using your phone or tablet<br>pillcheckhub will authenticate your medicine against the manufacturers own production records and pillcheckhub<br>will tell you immediately if your medicine is genuine</p>
  </section>
</div>
</body>
</html>
```